Brochure design for 3D ultrasound company

I am looking for a clean and modern and edgy brochure for my ultrasound company. We are a fairly new company specialize in 3D/4D ultrasounds.Our brochures will be placed in OB-GYN offices in high end areas around Los Angeles, so we need something that will stand out and capture a modern woman's attention. Our logo is currently in the process of being designed, so I don't have a picture to provide quite yet, however it will be our company name"Kite + Lantern" written in a special font that looks like neon lights. I will attach a few images of what our logo will be like, and some initial content that can help provide the layout we would like for the brochure. please feel free to also take a look at our website. www.kitelanternscan.example.

Target Market(s)

Upscale trendy women.

Colors
eea4c8
33a6d7
fee18a

Requirements
Should not have
• too many colors.

```html
<!DOCTYPE html>
<html lang="en">
<head>
<meta charset="utf-8">
<title>Kite + Lantern Trifold Brochure</title>
<link rel="stylesheet" href="https://fonts.googleapis.com/css2?family=Montserrat:wght@400;500;600;700&family=Great+Vibes&display=swap">
<style>
  :root {
    --page-bg: #d6d7da;
    --pink: #e98bb8;
    --pink-soft: #f4c4da;
    --pink-pale: #fbe3ee;
    --neon: #ea5fa8;
    --ink: #1d1d1f;
    --paper: #f6f6f7;
    --paper-shade: #e9e9ec;
    --white: #ffffff;
  }
  * { box-sizing: border-box; margin: 0; padding: 0; }
  html, body { width: 879px; height: 1200px; overflow: hidden; }
  body {
    background: var(--page-bg);
    font-family: "Montserrat", Arial, sans-serif;
    color: var(--ink);
    position: relative;
  }
  .spread {
    position: absolute;
    left: 121px;
    width: 648px;
    height: 504px;
    overflow: hidden;
    background: var(--paper);
  }
  .spread--outside { top: 67px; }
  .spread--inside { top: 623px; }
  .panel { position: absolute; top: 0; width: 216px; height: 504px; overflow: hidden; }
  .floral {
    background:
      radial-gradient(circle at 25% 30%, rgba(255,255,255,.7), transparent 35%),
      radial-gradient(circle at 75% 65%, rgba(255,255,255,.6), transparent 40%),
      radial-gradient(circle at 60% 20%, #f3a9cb, transparent 45%),
      linear-gradient(160deg, var(--pink-pale), var(--pink-soft) 50%, #f7d2e2);
  }
  .script {
    font-family: "Great Vibes", cursive;
    color: var(--neon);
    text-shadow: 0 0 6px rgba(234,95,168,.45);
    font-weight: 400;
  }
  .abs { position: absolute; }

  /* Panel: what's what */
  .panel--guide { left: 0; border-right: 1px solid var(--pink); }
  .guide__photo { position: absolute; left: 0; top: 0; width: 216px; height: 210px; }
  .guide__title { top: 204px; left: 0; width: 216px; text-align: center; font-size: 12px; font-weight: 600; letter-spacing: .5px; }
  .guide__body { top: 226px; left: 22px; width: 174px; font-size: 8.6px; line-height: 12.1px; text-align: justify; }
  .guide__body p { margin-bottom: 12px; }

  /* Panel: about */
  .panel--about {
    left: 216px;
    background: linear-gradient(90deg, var(--paper-shade), var(--paper) 12%, var(--paper) 88%, var(--paper-shade));
    text-align: center;
  }
  .about__name { top: 54px; left: 0; width: 216px; font-size: 17px; font-weight: 600; color: var(--neon); }
  .about__text { left: 18px; width: 180px; font-size: 9.6px; line-height: 13px; }
  .about__heading { left: 0; width: 216px; font-size: 30px; }
  .contact { top: 385px; left: 32px; list-style: none; font-size: 9px; line-height: 14.6px; text-align: left; }
  .contact li { display: flex; align-items: center; gap: 6px; }
  .contact .dot { width: 9px; height: 9px; border-radius: 50%; background: var(--pink); flex: none; }

  /* Panel: cover */
  .panel--cover { left: 432px; background: var(--white); }
  .cover__name { top: 20px; left: 0; width: 216px; text-align: center; font-size: 21px; font-weight: 600; letter-spacing: 2.5px; }
  .cover__tagline { top: 50px; left: 0; width: 216px; text-align: center; font-size: 9.5px; }
  .cover__photo { position: absolute; left: 0; top: 95px; width: 216px; height: 340px; }
  .cover__footer { position: absolute; left: 0; top: 400px; width: 216px; height: 104px; }
  .cover__claim { top: 427px; left: 0; width: 216px; text-align: center; font-size: 13px; font-weight: 600; line-height: 15px; }
  .cover__call {
    top: 461px; left: 30px; width: 165px; height: 19px; border-radius: 10px;
    background: var(--white); font-size: 9.5px; font-weight: 500;
    display: flex; align-items: center; justify-content: center;
  }
  .cover__web { top: 487px; left: 0; width: 216px; text-align: center; font-size: 7.6px; font-weight: 500; letter-spacing: .3px; }

  /* Inside: promo panel */
  .panel--promo { left: 0; border-right: 1px solid var(--pink); text-align: center; }
  .promo__offer { top: 93px; left: 10px; width: 196px; font-size: 12.5px; font-weight: 600; line-height: 17.5px; }
  .promo__rule { top: 271px; left: 16px; width: 184px; border-top: 1.5px dotted #555; }
  .promo__cta { top: 334px; left: 0; width: 216px; font-size: 11.5px; font-weight: 600; line-height: 17px; letter-spacing: .3px; }
  .promo__info { top: 399px; left: 6px; width: 204px; font-size: 8.6px; line-height: 14.6px; }

  /* Inside: services */
  .panel--services {
    left: 216px; width: 432px;
    background: linear-gradient(90deg, var(--paper-shade), var(--paper) 8%, var(--paper));
  }
  .services__photo { position: absolute; left: 0; top: 0; width: 432px; height: 225px; }
  .services__title { top: 52px; left: 90px; width: 260px; text-align: center; font-size: 36px; }
  .services__intro { top: 114px; left: 60px; width: 310px; text-align: center; font-size: 7.7px; line-height: 11px; }
  .package { left: 18px; width: 280px; }
  .package__name { font-size: 11.5px; font-weight: 600; color: var(--pink); letter-spacing: .8px; margin-bottom: 4px; }
  .package__list { list-style: none; font-size: 8.4px; line-height: 13px; }
  .package__list li { display: flex; align-items: center; gap: 6px; }
  .package__list li::before { content: ""; width: 6px; height: 6px; border-radius: 50%; background: var(--pink); flex: none; }
  .price {
    position: absolute; left: 266px; width: 56px; height: 14px; border-radius: 7px;
    background: var(--pink); color: var(--white); font-size: 8px; font-weight: 600;
    display: flex; align-items: center; justify-content: center;
  }
  .separator { left: 18px; width: 305px; border-top: 1.5px dotted var(--pink); }
  .moment {
    position: absolute; width: 98px; height: 98px; border-radius: 50%;
    border: 5px solid var(--pink-soft); left: 325px;
  }
</style>
</head>
<body>

<section class="spread spread--outside">

  <div class="panel panel--guide floral">
    <svg class="guide__photo" viewBox="0 0 216 210" role="img" aria-label="Photo of a pregnant belly held with an ultrasound print">
      <path d="M0 0H216V150Q130 170 0 210Z" fill="#d8b9a6"/>
      <path d="M0 210Q130 170 216 150" fill="none" stroke="#fff" stroke-width="5"/>
    </svg>
    <h2 class="abs guide__title">WHAT'S WHAT...</h2>
    <div class="abs guide__body">
      <p><b>2D</b> is the traditional black and white photo-you know, the one that you want to get emotional about, but you don't know what you're looking at.</p>
      <p><b>3D</b> is an image of the fetus and it's features. So you can see the baby has dad's nose, and mom's lips.</p>
      <p><b>4D</b> is 3D, but with motion. You can see the baby yawn, move it's arm, or even give you a smile.</p>
      <p><b>HD</b> is also 3D, but better. Now you can see a rendering of the baby's skin making it the most realistic fetal image possible.. we are one of the few in Los Angeles that have the newest HD capable machines</p>
    </div>
  </div>

  <div class="panel panel--about">
    <p class="abs about__name">Kite + Lantern</p>
    <p class="abs about__text" style="top:88px">Kite + Lantern is a mobile 3D ultrasound company servicing Los Angeles and surrounding areas.</p>
    <p class="abs about__text" style="top:152px">We take great pride in being one of LA's first mobile Ultrasound companies and for being an all female business!</p>
    <h2 class="abs about__heading script" style="top:222px">Our Mission</h2>
    <p class="abs about__text" style="top:268px">Our mission is to provide an unforgettable experience for expectant mothers in the comfort of their home!</p>
    <h2 class="abs about__heading script" style="top:339px">Contact Us</h2>
    <ul class="abs contact">
      <li><span class="dot"></span>310-555-0142</li>
      <li><span class="dot"></span>hello@kitelanternscan.example</li>
      <li><span class="dot"></span>www.kitelanternscan.example</li>
      <li><span class="dot"></span>@kitelanternscan</li>
      <li><span class="dot"></span>kite_lantern</li>
    </ul>
  </div>

  <div class="panel panel--cover">
    <h1 class="abs cover__name">Kite + Lantern</h1>
    <p class="abs cover__tagline">A mobile 3D/4D ultrasound service</p>
    <div class="cover__photo" role="img" aria-label="Photo of a pregnant woman sitting on a bed holding ultrasound prints" style="background:linear-gradient(180deg,#e9e7e6,#d9d3d0 45%,#ece9e8)"></div>
    <svg class="cover__footer" viewBox="0 0 216 104" role="img" aria-label="Soft pink floral backdrop">
      <defs>
        <linearGradient id="coverFloral" x1="0" y1="0" x2="1" y2="1">
          <stop offset="0" stop-color="#f8d6e6"/><stop offset=".5" stop-color="#f2b3cf"/><stop offset="1" stop-color="#f9dbe8"/>
        </linearGradient>
      </defs>
      <path d="M0 20Q110 -2 216 6V104H0Z" fill="url(#coverFloral)"/>
      <path d="M0 20Q110 -2 216 6" fill="none" stroke="#fff" stroke-width="3"/>
    </svg>
    <p class="abs cover__claim">Ultrasound in the comfort<br>of your home</p>
    <p class="abs cover__call">Call today!&nbsp; 310-555-0142</p>
    <p class="abs cover__web">www.kitelanternscan.example</p>
  </div>

  <svg class="abs" style="left:0;top:0" width="648" height="100" viewBox="0 0 648 100" aria-hidden="true">
    <path d="M333 0Q380 60 470 72Q560 82 648 88V100Q560 94 470 86Q375 74 333 0Z" fill="#e98bb8"/>
  </svg>
</section>

<section class="spread spread--inside">

  <div class="panel panel--promo floral">
    <p class="abs promo__offer">Enter code: “glow10“<br>at checkout and get<br>10% off<br>any package!</p>
    <div class="abs promo__rule"></div>
    <p class="abs promo__cta">READY FOR YOUR BABY'S<br>FIRST PHOTOSHOOT?</p>
    <p class="abs promo__info">Give us a call to schedule an appointment<br>310-555-0142<br>or visit our website<br>www.kitelanternscan.example</p>
  </div>

  <div class="panel panel--services">
    <svg class="services__photo" viewBox="0 0 432 225" role="img" aria-label="Photo of two pregnant women standing belly to belly">
      <defs>
        <linearGradient id="peachShot" x1="0" y1="0" x2="1" y2="0">
          <stop offset="0" stop-color="#e8b7a4"/><stop offset=".5" stop-color="#eec3b1"/><stop offset="1" stop-color="#e5b09c"/>
        </linearGradient>
      </defs>
      <path d="M0 0H432V180Q300 190 170 192Q60 196 0 225Z" fill="url(#peachShot)"/>
      <path d="M0 225Q60 196 170 192Q300 190 432 180" fill="none" stroke="#e98bb8" stroke-width="6"/>
    </svg>
    <h2 class="abs services__title script">Services + Pricing</h2>
    <p class="abs services__intro">We are available for private in-home screenings, gender reveals, baby showers, or any other special occasion!</p>

    <div class="abs package" style="top:227px">
      <h3 class="package__name">FIRST GLIMPSE:</h3>
      <ul class="package__list">
        <li>15 minute 2D session</li>
        <li>3 black and white images</li>
        <li>Listen to baby's heartbeat</li>
      </ul>
    </div>
    <span class="price" style="top:268px">$125.00</span>
    <div class="abs separator" style="top:287px"></div>

    <div class="abs package" style="top:300px">
      <h3 class="package__name">SWEET WAVE:</h3>
      <ul class="package__list">
        <li>15 minute 3D/4D /HD live session</li>
        <li>3 black and white images</li>
        <li>2 color images</li>
        <li>Listen to baby's heartbeat</li>
        <li>Confirm gender</li>
      </ul>
    </div>
    <span class="price" style="top:372px">$165.00</span>
    <div class="abs separator" style="top:388px"></div>

    <div class="abs package" style="top:399px">
      <h3 class="package__name">S.S. (STAR SESSION):</h3>
      <ul class="package__list">
        <li>30 min 3D/4D/HD live session on our projector</li>
        <li>10 color images</li>
        <li>Email or USB with all images</li>
        <li>Record and hear heartbeat</li>
        <li>Confirm gender</li>
      </ul>
    </div>
    <span class="price" style="top:472px">$325.00</span>

    <div class="moment" style="top:172px;background:radial-gradient(circle,#c9a08d,#b4826f)" role="img" aria-label="Photo of a belly with an ultrasound print"></div>
    <div class="moment" style="top:279px;background:radial-gradient(circle,#f3d7c6,#dcae92)" role="img" aria-label="Photo of a pregnant belly beside a plush toy"></div>
    <div class="moment" style="top:387px;background:radial-gradient(circle,#d7c3b6,#8795a8)" role="img" aria-label="Photo of a couple holding a tiny pair of baby shoes"></div>
  </div>
</section>

</body>
</html>
```